Create a professional, eye-catching business card design that reflects the values and services of Brookfern Veterinary Hospital. we provide veterinary services and the business card should be a memorable representation of the clinic and align with its branding and mission. our tag line is "Life Long Companions, Lifelong Care"
Use clean, modern typography. Prioritize readability and professionalism. We would like to see designs that use the color blue, as in the logo example. the final design should communicate professionalism and care, with attention to detail.

```html
<!DOCTYPE html>
<html lang="en">
<head>
<meta charset="utf-8">
<title>Brookfern Veterinary Hospital – Business Card</title>
<link href="https://fonts.googleapis.com/css2?family=Montserrat:wght@400;500;700;800&display=swap" rel="stylesheet">
<style>
  :root {
    --navy: #1f3464;
    --white: #ffffff;
    --backdrop: #6e6f75;
    --backdrop-edge: #3d3e43;
  }
  * { margin: 0; padding: 0; box-sizing: border-box; }
  html, body { width: 1200px; height: 780px; overflow: hidden; }
  body {
    background: radial-gradient(ellipse at 45% 45%, var(--backdrop) 0%, var(--backdrop-edge) 100%);
    font-family: 'Montserrat', sans-serif;
    position: relative;
  }
  .card {
    position: absolute;
    top: 236px;
    width: 540px;
    height: 309px;
    overflow: hidden;
    box-shadow: 0 12px 28px rgba(0,0,0,0.35);
  }
  .card--front { left: 40px; background: var(--navy); }
  .card--back { left: 620px; background: var(--white); }
  .card__art { position: absolute; inset: 0; }

  .brand {
    position: absolute;
    display: flex;
    align-items: center;
    gap: 10px;
  }
  .brand__dot {
    width: 34px; height: 34px;
    border-radius: 50%;
    border: 2px solid currentColor;
    flex: none;
  }
  .brand__name {
    font-weight: 700;
    font-size: 15px;
    line-height: 1.15;
    text-transform: uppercase;
    letter-spacing: 0.5px;
  }
  .card--front .brand { top: 44px; right: 34px; color: var(--white); }
  .card--back .brand { top: 96px; left: 40px; color: var(--navy); }

  .tagline {
    position: absolute;
    right: 30px;
    bottom: 26px;
    color: var(--navy);
    font-size: 14px;
    letter-spacing: 0.8px;
    font-weight: 400;
  }
  .tagline strong { font-weight: 800; }

  .holder {
    position: absolute;
    top: 40px;
    right: 32px;
    color: var(--navy);
    font-size: 21px;
    font-weight: 400;
  }
  .holder strong { font-weight: 800; }

  .contacts {
    position: absolute;
    left: 44px;
    top: 168px;
    list-style: none;
    color: var(--navy);
    font-size: 12.5px;
    font-weight: 500;
  }
  .contacts li { display: flex; align-items: center; gap: 8px; margin-bottom: 7px; }
  .contacts svg { width: 12px; height: 12px; flex: none; }

  .address {
    position: absolute;
    left: 44px;
    bottom: 12px;
    color: var(--white);
    font-size: 12.5px;
    font-weight: 500;
    display: flex; align-items: center; gap: 8px;
  }
  .address svg { width: 11px; height: 13px; }
</style>
</head>
<body>

  <section class="card card--front" aria-label="Card front">
    <svg class="card__art" viewBox="0 0 540 309" aria-hidden="true">
      <path d="M0,309 L0,250 C60,238 100,232 150,226 L330,200 C400,185 470,165 540,140 L540,309 Z" fill="var(--white)"/>
    </svg>
    <svg class="card__art" viewBox="0 0 540 309">
      <rect role="img" aria-label="White silhouettes of a dog and a cat sitting on a hill, looking up" x="100" y="62" width="200" height="172" rx="40" fill="var(--white)" opacity="0.9"/>
    </svg>
    <div class="brand">
      <span class="brand__dot"></span>
      <span class="brand__name">Brookfern<br>Veterinary Hospital</span>
    </div>
    <p class="tagline">LIFE LONG COMPANIONS, <strong>LIFELONG CARE</strong></p>
  </section>

  <section class="card card--back" aria-label="Card back">
    <svg class="card__art" viewBox="0 0 540 309" aria-hidden="true">
      <path d="M230,309 C270,280 300,262 340,236 C400,210 470,195 540,178 L540,309 Z" fill="var(--navy)"/>
      <rect x="0" y="270" width="540" height="39" fill="var(--navy)"/>
    </svg>
    <svg class="card__art" viewBox="0 0 540 309">
      <rect role="img" aria-label="Navy silhouettes of a dog and a cat sitting on a hill, looking up" x="330" y="88" width="160" height="150" rx="36" fill="var(--navy)"/>
    </svg>

    <p class="holder"><strong>Daniel Marsh,</strong> DVM</p>

    <div class="brand">
      <span class="brand__dot"></span>
      <span class="brand__name">Brookfern<br>Veterinary Hospital</span>
    </div>

    <ul class="contacts">
      <li>
        <svg viewBox="0 0 24 24" aria-hidden="true"><path fill="var(--navy)" d="M6.6 10.8a15 15 0 0 0 6.6 6.6l2.2-2.2c.3-.3.7-.4 1-.2 1.1.4 2.3.6 3.6.6.6 0 1 .4 1 1V20c0 .6-.4 1-1 1A17 17 0 0 1 3 4c0-.6.4-1 1-1h3.5c.6 0 1 .4 1 1 0 1.3.2 2.5.6 3.6.1.3 0 .7-.2 1z"/></svg>
        (08) 9361 4820
      </li>
      <li>
        <svg viewBox="0 0 24 24" aria-hidden="true"><rect x="2" y="5" width="20" height="14" fill="var(--navy)"/><path d="M2 5l10 8 10-8" stroke="var(--white)" stroke-width="1.6" fill="none"/></svg>
        reception@brookfernvet.com.au
      </li>
      <li>
        <svg viewBox="0 0 24 24" aria-hidden="true"><circle cx="12" cy="12" r="10" fill="none" stroke="var(--navy)" stroke-width="2"/><ellipse cx="12" cy="12" rx="4.5" ry="10" fill="none" stroke="var(--navy)" stroke-width="2"/><path d="M2 12h20" stroke="var(--navy)" stroke-width="2"/></svg>
        www.brookfernvet.com.au
      </li>
    </ul>

    <p class="address">
      <svg viewBox="0 0 20 24" aria-hidden="true"><path fill="var(--white)" d="M10 0a9 9 0 0 0-9 9c0 6.5 9 15 9 15s9-8.5 9-15a9 9 0 0 0-9-9zm0 12.5a3.5 3.5 0 1 1 0-7 3.5 3.5 0 0 1 0 7z"/></svg>
      12 Ridgeview Road, Glenmore, WA 6099
    </p>
  </section>

</body>
</html>
```